Flyer für IT-Firma
Zielgruppe
Wir sind eine IT-Firma, die sich unter anderem auf IT-Netzwerke spezialisiert hat. Wir verkaufen Netzwerklösungen, aber auch Produkte im Bereich IT Netzwerk, IT Security, WLAN, Cloud-Lösungen, etc. und Services. Unsere Zielgruppen für diesen Bereich sind kleinere bis Mittlere Unternehmen aber auch öffentliche Verwaltungen, Schulen, Spitäler etc. die ihre IT Netzwerke verbessern möchten und sich absichern möchten für den Fall von WLAN Ausfall oder Datenverlust. Diese Zielgruppen kennen uns womöglich noch nicht oder haben in einem anderen Projekt mit uns zusammengearbeitet. Der Flyer soll sie also von uns und dem Produkt überzeugen.
Aufgabenstellung
Der Flyer soll 2-Seitig oder 4-Seitig sein. Er soll als Vorlage für die Präsentation verschiedenster Produkte dienen. Ziel ist es einen Flyer zu haben im einheitlichen Design, den wir beliebig mit Fotos und Text abfüllen können. So dass wir unsere Produkte und Dienstleistungen im einheitlichen Design vorstellen können. Der Flyer soll folgende Elemente beinhalten:
Seite 1 eher oberflächlich das Produkt vorstellen
- Logo
- Einleitung zum Unternehmen und oder Produkt
- 1-2 Platzhalter für Bilder
- Weiterer Text für Produktbeschreibung
Seite 2 detaillierte Informationen:
- technische Daten (allenfalls in Listenform)
- Weitere Detailinformationen
- Preise
- Kontakt
Vorzugsweise Format A4 damit man auch daraus einfach ein PDF generieren kann und per Mail versenden kann. Vorschläge für andere Formate sind willkommen.

```html
<!DOCTYPE html>
<html lang="de">
<head>
<meta charset="utf-8">
<title>Flyer Vorlage – nordlink systems</title>
<link href="https://fonts.googleapis.com/css2?family=Montserrat:ital,wght@0,400;0,600;0,700;0,800;1,400&display=swap" rel="stylesheet">
<style>
:root{
  --teal:#177f7c;
  --teal-dark:#0f5f5d;
  --green:#6ab13c;
  --orange:#f0a01c;
  --ink:#3a3f44;
  --muted:#8a8f94;
  --mint:#eaf4f1;
  --foot:#c9cbcc;
  --board:#f2f2f2;
  --hero-a:#06233a;
  --hero-b:#0f6f8c;
  --hero-c:#38b4d6;
}
*{box-sizing:border-box;margin:0;padding:0}
html,body{width:723px;height:1200px;overflow:hidden}
body{background:var(--board);font-family:'Montserrat',sans-serif;color:var(--ink);position:relative}

.slot{position:absolute;width:325px;height:459px;transform-origin:0 0;background:#fff;overflow:hidden;box-shadow:0 1px 3px rgba(0,0,0,.08)}
.scale-lg{transform:scale(.62)}
.scale-sm{transform:scale(.487)}
.p-top-a{left:150px;top:88px}
.p-top-b{left:372px;top:88px}
.p-r1a{left:116px;top:440px}
.p-r1b{left:286px;top:440px}
.p-r1c{left:458px;top:440px}
.p-r2a{left:201px;top:681px}
.p-r2b{left:373px;top:681px}
.p-r3a{left:32px;top:921px}
.p-r3b{left:201px;top:921px}
.p-r3c{left:371px;top:921px}
.p-r3d{left:541px;top:921px}

/* brand */
.brand{height:48px;display:flex;flex-direction:column;align-items:center;justify-content:center}
.brand .row{display:flex;align-items:center;gap:5px}
.brand .mark{width:9px;height:9px;background:var(--teal)}
.brand .name{font-size:15px;font-weight:600;color:#555a5f;letter-spacing:-.2px}
.brand .sub{font-size:6px;color:var(--muted);margin-top:-1px}

/* front page */
.hero{height:120px;background:radial-gradient(circle at 45% 35%,var(--hero-c) 0,var(--hero-b) 22%,var(--hero-a) 70%)}
.band{height:30px;margin-top:-10px;margin-left:0;background:var(--teal);color:#fff;font-size:13.5px;font-weight:800;text-align:center;line-height:30px;border-top-left-radius:14px;border-top-right-radius:0;position:relative}
.about{padding:9px 18px 8px;text-align:center}
.about h2{font-size:6.5px;color:var(--teal);font-weight:700;margin-bottom:5px}
.tiny{font-size:3.6px;line-height:1.75;color:#555}
.body{position:absolute;left:0;right:0;top:270px;bottom:10px;background:var(--mint)}
.foot{position:absolute;left:0;right:0;bottom:0;height:12px;background:var(--foot);display:flex;justify-content:space-between;align-items:center;padding:0 18px;font-size:3px;color:#fff;font-weight:600}
h3.ph{font-size:5.5px;color:var(--teal);font-weight:700;margin-bottom:4px}
.pic{background:radial-gradient(circle at 50% 45%,#bfe9f7 0,var(--hero-c) 14%,var(--hero-b) 38%,var(--hero-a) 80%)}
.card{border:3px solid #fff;border-radius:6px;box-shadow:0 2px 5px rgba(0,0,0,.25)}
ul.ticks{list-style:none;margin-top:3px}
ul.ticks li{position:relative;padding-left:8px;margin-bottom:3px}
ul.ticks li::before{content:"";position:absolute;left:0;top:2px;width:3px;height:3px;border-radius:50%;background:var(--green)}

.v1{display:flex;gap:12px;padding:14px 12px 0 22px}
.v1 .pic{width:108px;height:138px;flex:none}
.v2{padding:6px 20px 0 28px}
.v2 .rowx{display:flex;gap:12px;align-items:flex-start;margin-bottom:6px}
.v2 .pic{width:98px;height:68px;flex:none}
.v3{display:flex;gap:10px;padding:0 18px}
.v3 .col{flex:1}
.v3 .pic{height:58px;margin-bottom:8px}
.v3 ul.ticks li{margin-bottom:7px}
.v4{display:flex;background:#fff}
.v4 .pic{width:145px;flex:none}
.v4 .txt{padding:6px 14px}
.quote{display:flex;gap:4px;margin-top:8px;font-style:italic}
.quote .qm{font-size:16px;color:#c8cdd0;line-height:1;font-style:normal}

/* back page */
.tab{position:absolute;left:0;top:9px;height:18px;width:156px;background:var(--teal);color:#fff;font-size:6.5px;font-weight:800;line-height:18px;padding-left:21px;border-radius:0 9px 9px 0}
.tech{position:absolute;left:25px;right:22px;top:36px;display:flex;gap:16px}
.tech .left{width:130px}
.tech .right{flex:1}
h4.sh{font-size:4.2px;color:var(--teal);font-weight:700;margin-bottom:5px}
table.spec{width:100%;border-collapse:collapse;font-size:3.1px;color:#555}
table.spec th{color:var(--teal);text-align:left;font-weight:600;padding-bottom:2px}
table.spec td{padding:1.2px 0}
.why{position:absolute;left:0;right:0;top:170px;height:108px;background:var(--mint);padding:12px 25px}
.why .cols{display:flex;gap:12px}
.why .cols>*{flex:1}
.prices{position:absolute;left:0;right:0;top:292px;display:flex;justify-content:center;gap:10px}
.price{width:52px;text-align:center}
.price .tag{display:block;height:6px;border-radius:2px;font-size:2.8px;font-weight:700;color:#fff;line-height:6px}
.price .amt{font-size:13px;font-weight:700;margin:3px 0 2px}
.price .cap{font-size:2.7px;line-height:1.5;color:#777}
.basic .tag{background:var(--ink)} .basic .amt{color:var(--ink)}
.advance .tag{background:var(--green)} .advance .amt{color:var(--green)}
.company .tag{background:var(--orange)} .company .amt{color:var(--orange)}
.enterprise .tag{background:var(--teal)} .enterprise .amt{color:var(--teal)}
.contact{position:absolute;left:25px;right:14px;top:385px;display:flex;gap:10px}
.contact .logo-col{width:110px}
.contact .brand{height:auto;align-items:flex-start}
.partners{display:flex;flex-wrap:wrap;gap:4px;margin-top:6px;align-items:center}
.partners .lbl{font-size:2.6px;color:#888;width:22px;line-height:1.3}
.partners .chip{width:17px;height:5px;background:#b9bec2;border-radius:1px}
.partners .chip.red{background:#d8464a}
.partners .chip.blue{background:#4f8ec6}
.addr{width:68px;font-size:2.8px;line-height:1.6;color:#666}
.addr b{display:block;color:var(--green);font-size:3.4px;margin-bottom:1px}
.why.split{display:flex;gap:14px}
.why.split .l{width:130px}
.why.split .r{flex:1;text-align:center}
.grid4{display:grid;grid-template-columns:1fr 1fr;gap:8px 8px;margin-top:6px}
.grid4 .price{width:auto}
</style>
</head>
<body>

<!-- hero pair -->
<article class="slot scale-lg p-top-a">
  <div class="tab">PRODUCT TECHNICAL DATA</div>
  <div class="tech">
    <div class="left"><h4 class="sh">Production Description</h4><p class="tiny">Lorem ipsum dolor sit amet, consectetuer adipiscing elit, sed diam nonummy nibh euismod tincidunt ut laoreet dolore magna aliquam erat volutpat. Ut wisi enim ad minim veniam, quis nostrud exerci tation ullamcorper suscipit lobortis nisl ut aliquip ex ea commodo consequat.</p><p class="tiny" style="margin-top:5px">Lorem ipsum dolor sit amet, consectetuer adipiscing elit, sed diam nonummy nibh euismod.</p></div>
    <div class="right"><h4 class="sh">Product Specification</h4>
      <table class="spec"><tr><th>Format</th><th>Size</th><th>Metric</th><th>Xx</th></tr>
      <tr><td>Lorem ipsum</td><td>12</td><td>cm</td><td>-</td></tr><tr><td>Lorem ipsum</td><td>256</td><td>mm</td><td>-</td></tr><tr><td>Lorem ipsum</td><td>7128</td><td>mm</td><td>-</td></tr><tr><td>Lorem ipsum</td><td>092</td><td>cm</td><td>-</td></tr><tr><td>Lorem ipsum</td><td>67</td><td>mm</td><td>-</td></tr><tr><td>Lorem ipsum</td><td>89</td><td>mm</td><td>-</td></tr><tr><td>Lorem ipsum</td><td>90</td><td>mm</td><td>-</td></tr><tr><td>Lorem ipsum</td><td>309</td><td>mm</td><td>-</td></tr><tr><td>Lorem ipsum</td><td>596</td><td>mm</td><td>-</td></tr></table></div>
  </div>
  <div class="why"><h4 class="sh">Why you should buy this product?</h4><div class="cols"><p class="tiny">Lorem ipsum dolor sit amet, consectetuer adipiscing elit, sed diam nonummy nibh euismod tincidunt ut laoreet dolore magna aliquam erat volutpat. Ut wisi enim ad minim veniam.</p><p class="tiny">Lorem ipsum dolor sit amet, consectetuer adipiscing elit, sed diam nonummy nibh euismod tincidunt ut laoreet dolore magna aliquam erat volutpat.</p></div></div>
  <div class="prices"><div class="price basic"><span class="tag">BASIC</span><div class="amt">€100</div><p class="cap">Lorem ipsum dolor sit amet, consectetuer adipiscing elit</p></div><div class="price advance"><span class="tag">ADVANCE</span><div class="amt">€600</div><p class="cap">Lorem ipsum dolor sit amet, consectetuer adipiscing elit</p></div><div class="price company"><span class="tag">COMPANY</span><div class="amt">€2500</div><p class="cap">Lorem ipsum dolor sit amet, consectetuer adipiscing elit</p></div></div>
  <div class="contact"><div class="logo-col"><div class="brand"><div class="row"><span class="mark"></span><span class="name">nordlink systems</span></div><span class="sub">by netwave</span></div><div class="partners"><span class="lbl">Mit unsere starken Partnern</span><span class="chip"></span><span class="chip blue"></span><span class="chip red"></span><span class="chip"></span><span class="chip blue"></span><span class="chip red"></span></div></div>
  <div class="addr"><b>Hauptsitz</b>Netwave AG<br>Lindenweg 8<br>6300 Seefeld<br>Telefon +41 00 000 10 10<br>info@netwave-demo.ch</div>
  <div class="addr"><b>Niederlassung</b>Netwave AG<br>Haus am Hang, Rue du Lac 12<br>1260 Valmont<br>Telefon +41 00 000 10 20<br>info@netwave-demo.ch</div></div>
</article>

<article class="slot scale-lg p-top-b">
  <header class="brand"><div class="row"><span class="mark"></span><span class="name">nordlink systems</span></div><span class="sub">by netwave</span></header>
  <div class="hero" role="img" aria-label="Photo: hand touching a glowing globe surrounded by network icons"></div>
  <h1 class="band">VERBUNDEN MIT DER ZUKUNFT</h1>
  <section class="about"><h2>About Our Company</h2><p class="tiny">Netwave ist ein Schweizer Unternehmen, das sich auf massgeschneiderte Netzwerklösungen für Geschäftskunden spezialisiert hat. Mit über 30 Jahren Erfahrung und starken Partnern entwickeln wir zukunftsorientierte IT-Infrastrukturen. Unsere Experten begleiten Sie von der Planung bis zur Umsetzung und bieten 24-Stunden-Support für reibungslose Abläufe. Vertrauen Sie auf unsere Kompetenz in Netzwerken, Security, WLAN und IoT.</p></section>
  <section class="body v1"><div class="pic card" role="img" aria-label="Photo: hands holding a glowing globe"></div><div><h3 class="ph">Ihr Produkte Name</h3><p class="tiny">Lorem ipsum dolor sit amet, consectetuer adipiscing elit, sed diam nonummy nibh euismod tincidunt ut laoreet dolore magna.</p><ul class="ticks tiny"><li>Lorem ipsum dolor sit amet, consectetuer adipiscing elit, sed diam nonummy nibh euismod tincidunt ut laoreet dolore magna aliquam erat volutpat.</li><li>Ut wisi enim ad minim veniam, quis nostrud exerci tation ullam corper suscipit lobortis nisl ut aliquip ex ea commodo consequat.</li><li>Duis autem vel eum iriure dolor in hendrerit in vulputate velit esse molestie consequat, vel illum dolore eu feugiat nulla facilisis.</li></ul></div></section>
  <footer class="foot"><span>nordlink systems by netwave | Your Slogan goes here</span><span>www.netwave-demo.ch</span></footer>
</article>

<!-- front variants -->
<article class="slot scale-sm p-r1a">
  <header class="brand"><div class="row"><span class="mark"></span><span class="name">nordlink systems</span></div><span class="sub">by netwave</span></header>
  <div class="hero" role="img" aria-label="Photo: hand touching a glowing globe surrounded by network icons"></div>
  <h1 class="band">VERBUNDEN MIT DER ZUKUNFT</h1>
  <section class="about"><h2>About Our Company</h2><p class="tiny">Netwave ist ein Schweizer Unternehmen, das sich auf massgeschneiderte Netzwerklösungen für Geschäftskunden spezialisiert hat. Mit über 30 Jahren Erfahrung und starken Partnern entwickeln wir zukunftsorientierte IT-Infrastrukturen. Unsere Experten begleiten Sie von der Planung bis zur Umsetzung und bieten 24-Stunden-Support für reibungslose Abläufe. Vertrauen Sie auf unsere Kompetenz in Netzwerken, Security, WLAN und IoT.</p></section>
  <section class="body v1"><div class="pic card" role="img" aria-label="Photo: hands holding a glowing globe"></div><div><h3 class="ph">Ihr Produkte Name</h3><p class="tiny">Lorem ipsum dolor sit amet, consectetuer adipiscing elit, sed diam nonummy nibh euismod tincidunt ut laoreet dolore magna.</p><ul class="ticks tiny"><li>Lorem ipsum dolor sit amet, consectetuer adipiscing elit, sed diam nonummy nibh euismod tincidunt ut laoreet dolore magna aliquam erat volutpat.</li><li>Ut wisi enim ad minim veniam, quis nostrud exerci tation ullam corper suscipit lobortis nisl ut aliquip ex ea commodo consequat.</li><li>Duis autem vel eum iriure dolor in hendrerit in vulputate velit esse molestie consequat, vel illum dolore eu feugiat nulla facilisis.</li></ul></div></section>
  <footer class="foot"><span>nordlink systems by netwave | Your Slogan goes here</span><span>www.netwave-demo.ch</span></footer>
</article>

<article class="slot scale-sm p-r1b">
  <header class="brand"><div class="row"><span class="mark"></span><span class="name">nordlink systems</span></div><span class="sub">by netwave</span></header>
  <div class="hero" role="img" aria-label="Photo: hand touching a glowing globe surrounded by network icons"></div>
  <h1 class="band">VERBUNDEN MIT DER ZUKUNFT</h1>
  <section class="about"><h2>About Our Company</h2><p class="tiny">Netwave ist ein Schweizer Unternehmen, das sich auf massgeschneiderte Netzwerklösungen für Geschäftskunden spezialisiert hat. Mit über 30 Jahren Erfahrung und starken Partnern entwickeln wir zukunftsorientierte IT-Infrastrukturen. Unsere Experten begleiten Sie von der Planung bis zur Umsetzung und bieten 24-Stunden-Support für reibungslose Abläufe. Vertrauen Sie auf unsere Kompetenz in Netzwerken, Security, WLAN und IoT.</p></section>
  <section class="body v2">
    <div class="rowx"><div class="pic card" role="img" aria-label="Photo: hands holding a glowing globe"></div><div><h3 class="ph">Ihr Produkte Name</h3><p class="tiny">Lorem ipsum dolor sit amet, consectetuer adipiscing elit, sed diam nonummy nibh euismod tincidunt ut laoreet dolore magna.</p><ul class="ticks tiny"><li>Lorem ipsum dolor sit amet, consectetuer adipiscing elit, sed diam nonummy nibh euismod tincidunt ut laoreet dolore magna aliquam erat volutpat.</li></ul></div></div>
    <div class="rowx"><div><h3 class="ph">Ihr Produkte Name</h3><p class="tiny">Lorem ipsum dolor sit amet, consectetuer adipiscing elit, sed diam nonummy nibh euismod tincidunt ut laoreet dolore magna.</p><ul class="ticks tiny"><li>Lorem ipsum dolor sit amet, consectetuer adipiscing elit, sed diam nonummy nibh euismod tincidunt ut laoreet dolore magna aliquam erat volutpat.</li></ul></div><div class="pic card" role="img" aria-label="Photo: hands holding a glowing globe"></div></div>
  </section>
  <footer class="foot"><span>nordlink systems by netwave | Your Slogan goes here</span><span>www.netwave-demo.ch</span></footer>
</article>

<article class="slot scale-sm p-r1c">
  <header class="brand"><div class="row"><span class="mark"></span><span class="name">nordlink systems</span></div><span class="sub">by netwave</span></header>
  <div class="hero" role="img" aria-label="Photo: hand touching a glowing globe surrounded by network icons"></div>
  <h1 class="band">VERBUNDEN MIT DER ZUKUNFT</h1>
  <section class="about"><h2>About Our Company</h2><p class="tiny">Netwave ist ein Schweizer Unternehmen, das sich auf massgeschneiderte Netzwerklösungen für Geschäftskunden spezialisiert hat. Mit über 30 Jahren Erfahrung und starken Partnern entwickeln wir zukunftsorientierte IT-Infrastrukturen. Unsere Experten begleiten Sie von der Planung bis zur Umsetzung und bieten 24-Stunden-Support für reibungslose Abläufe. Vertrauen Sie auf unsere Kompetenz in Netzwerken, Security, WLAN und IoT.</p></section>
  <section class="body v3" style="padding-top:8px">
    <div class="col"><div class="pic card" role="img" aria-label="Photo: hands holding a glowing globe"></div><ul class="ticks tiny"><li>Lorem ipsum dolor sit amet, consectetuer adipiscing elit, sed diam nonummy nibh euismod tincidunt ut laoreet dolore.</li><li>Lorem ipsum dolor sit amet, consectetuer adipiscing elit, sed diam nonummy nibh euismod tincidunt ut laoreet dolore.</li></ul></div>
    <div class="col"><div class="pic card" role="img" aria-label="Photo: hands holding a glowing globe"></div><ul class="ticks tiny"><li>Lorem ipsum dolor sit amet, consectetuer adipiscing elit, sed diam nonummy nibh euismod tincidunt ut laoreet dolore.</li><li>Lorem ipsum dolor sit amet, consectetuer adipiscing elit, sed diam nonummy nibh euismod tincidunt ut laoreet dolore.</li></ul></div>
    <div class="col"><div class="pic card" role="img" aria-label="Photo: hands holding a glowing globe"></div><ul class="ticks tiny"><li>Lorem ipsum dolor sit amet, consectetuer adipiscing elit, sed diam nonummy nibh euismod tincidunt ut laoreet dolore.</li><li>Lorem ipsum dolor sit amet, consectetuer adipiscing elit, sed diam nonummy nibh euismod tincidunt ut laoreet dolore.</li></ul></div>
  </section>
  <footer class="foot"><span>nordlink systems by netwave | Your Slogan goes here</span><span>www.netwave-demo.ch</span></footer>
</article>

<article class="slot scale-sm p-r2a">
  <header class="brand"><div class="row"><span class="mark"></span><span class="name">nordlink systems</span></div><span class="sub">by netwave</span></header>
  <div class="hero" role="img" aria-label="Photo: hand touching a glowing globe surrounded by network icons"></div>
  <h1 class="band">VERBUNDEN MIT DER ZUKUNFT</h1>
  <section class="about"><h2>About Our Company</h2><p class="tiny">Netwave ist ein Schweizer Unternehmen, das sich auf massgeschneiderte Netzwerklösungen für Geschäftskunden spezialisiert hat. Mit über 30 Jahren Erfahrung und starken Partnern entwickeln wir zukunftsorientierte IT-Infrastrukturen. Unsere Experten begleiten Sie von der Planung bis zur Umsetzung und bieten 24-Stunden-Support für reibungslose Abläufe. Vertrauen Sie auf unsere Kompetenz in Netzwerken, Security, WLAN und IoT.</p></section>
  <section class="body v4"><div class="pic" role="img" aria-label="Photo: hands holding a glowing globe"></div><div class="txt"><h3 class="ph">Your text goes here</h3><p class="tiny">Lorem ipsum dolor sit amet, consectetuer adipiscing elit, sed diam nonummy nibh euismod tincidunt ut laoreet dolore magna aliquam erat volutpat. Ut wisi enim ad minim veniam, quis nostrud exerci tation ullamcorper suscipit lobortis nisl ut aliquip ex ea commodo consequat. Duis autem vel eum iriure dolor in hendrerit in vulputate velit esse.</p><div class="quote"><span class="qm">“</span><p class="tiny">Lorem ipsum dolor sit amet, consectetuer adipiscing elit, sed diam nonummy nibh euismod tincidunt ut laoreet dolore magna aliquam erat volutpat. Ut wisi enim ad minim veniam, quis nostrud exerci tation ullamcorper suscipit lobortis nisl ut aliquip ex ea commodo consequat.</p></div></div></section>
  <footer class="foot"><span>nordlink systems by netwave | Your Slogan goes here</span><span>www.netwave-demo.ch</span></footer>
</article>

<article class="slot scale-sm p-r2b">
  <header class="brand"><div class="row"><span class="mark"></span><span class="name">nordlink systems</span></div><span class="sub">by netwave</span></header>
  <div class="hero" role="img" aria-label="Photo: hand touching a glowing globe surrounded by network icons"></div>
  <h1 class="band">VERBUNDEN MIT DER ZUKUNFT</h1>
  <section class="about"><h2>About Our Company</h2><p class="tiny">Netwave ist ein Schweizer Unternehmen, das sich auf massgeschneiderte Netzwerklösungen für Geschäftskunden spezialisiert hat. Mit über 30 Jahren Erfahrung und starken Partnern entwickeln wir zukunftsorientierte IT-Infrastrukturen. Unsere Experten begleiten Sie von der Planung bis zur Umsetzung und bieten 24-Stunden-Support für reibungslose Abläufe. Vertrauen Sie auf unsere Kompetenz in Netzwerken, Security, WLAN und IoT.</p></section>
  <section class="body v4"><div class="txt"><h3 class="ph">Your text goes here</h3><p class="tiny">Lorem ipsum dolor sit amet, consectetuer adipiscing elit, sed diam nonummy nibh euismod tincidunt ut laoreet dolore magna aliquam erat volutpat. Ut wisi enim ad minim veniam, quis nostrud exerci tation ullamcorper suscipit lobortis nisl ut aliquip ex ea commodo consequat. Duis autem vel eum iriure dolor in hendrerit in vulputate velit esse.</p><div class="quote"><span class="qm">“</span><p class="tiny">Lorem ipsum dolor sit amet, consectetuer adipiscing elit, sed diam nonummy nibh euismod tincidunt ut laoreet dolore magna aliquam erat volutpat. Ut wisi enim ad minim veniam, quis nostrud exerci tation ullamcorper suscipit lobortis nisl ut aliquip ex ea commodo consequat.</p></div></div><div class="pic" role="img" aria-label="Photo: hands holding a glowing globe"></div></section>
  <footer class="foot"><span>nordlink systems by netwave | Your Slogan goes here</span><span>www.netwave-demo.ch</span></footer>
</article>

<!-- back variants -->
<article class="slot scale-sm p-r3a">
  <div class="tab">PRODUCT TECHNICAL DATA</div>
  <div class="tech"><div class="left"><h4 class="sh">Production Description</h4><p class="tiny">Lorem ipsum dolor sit amet, consectetuer adipiscing elit, sed diam nonummy nibh euismod tincidunt ut laoreet dolore magna aliquam erat volutpat. Ut wisi enim ad minim veniam, quis nostrud exerci tation ullamcorper suscipit lobortis nisl ut aliquip ex ea commodo consequat.</p><p class="tiny" style="margin-top:5px">Lorem ipsum dolor sit amet, consectetuer adipiscing elit, sed diam nonummy nibh euismod.</p></div>
  <div class="right"><h4 class="sh">Product Specification</h4><table class="spec"><tr><th>Format</th><th>Size</th><th>Metric</th><th>Xx</th></tr><tr><td>Lorem ipsum</td><td>12</td><td>cm</td><td>-</td></tr><tr><td>Lorem ipsum</td><td>256</td><td>mm</td><td>-</td></tr><tr><td>Lorem ipsum</td><td>7128</td><td>mm</td><td>-</td></tr><tr><td>Lorem ipsum</td><td>092</td><td>cm</td><td>-</td></tr><tr><td>Lorem ipsum</td><td>67</td><td>mm</td><td>-</td></tr><tr><td>Lorem ipsum</td><td>89</td><td>mm</td><td>-</td></tr><tr><td>Lorem ipsum</td><td>90</td><td>mm</td><td>-</td></tr><tr><td>Lorem ipsum</td><td>309</td><td>mm</td><td>-</td></tr><tr><td>Lorem ipsum</td><td>596</td><td>mm</td><td>-</td></tr></table></div></div>
  <div class="why"><h4 class="sh">Why you should buy this product?</h4><div class="cols"><p class="tiny">Lorem ipsum dolor sit amet, consectetuer adipiscing elit, sed diam nonummy nibh euismod tincidunt ut laoreet dolore magna aliquam erat volutpat. Ut wisi enim ad minim veniam.</p><p class="tiny">Lorem ipsum dolor sit amet, consectetuer adipiscing elit, sed diam nonummy nibh euismod tincidunt ut laoreet dolore magna aliquam erat volutpat.</p></div></div>
  <div class="prices"><div class="price basic"><span class="tag">BASIC</span><div class="amt">€100</div><p class="cap">Lorem ipsum dolor sit amet, consectetuer adipiscing elit</p></div><div class="price advance"><span class="tag">ADVANCE</span><div class="amt">€600</div><p class="cap">Lorem ipsum dolor sit amet, consectetuer adipiscing elit</p></div></div>
  <div class="contact"><div class="logo-col"><div class="brand"><div class="row"><span class="mark"></span><span class="name">nordlink systems</span></div><span class="sub">by netwave</span></div><div class="partners"><span class="lbl">Mit unsere starken Partnern</span><span class="chip"></span><span class="chip blue"></span><span class="chip red"></span><span class="chip"></span><span class="chip blue"></span><span class="chip red"></span></div></div>
  <div class="addr"><b>Hauptsitz</b>Netwave AG<br>Lindenweg 8<br>6300 Seefeld<br>Telefon +41 00 000 10 10<br>info@netwave-demo.ch</div><div class="addr"><b>Niederlassung</b>Netwave AG<br>Haus am Hang, Rue du Lac 12<br>1260 Valmont<br>Telefon +41 00 000 10 20<br>info@netwave-demo.ch</div></div>
</article>

<article class="slot scale-sm p-r3b">
  <div class="tab">PRODUCT TECHNICAL DATA</div>
  <div class="tech"><div class="left"><h4 class="sh">Production Description</h4><p class="tiny">Lorem ipsum dolor sit amet, consectetuer adipiscing elit, sed diam nonummy nibh euismod tincidunt ut laoreet dolore magna aliquam erat volutpat. Ut wisi enim ad minim veniam, quis nostrud exerci tation ullamcorper suscipit lobortis nisl ut aliquip ex ea commodo consequat.</p><p class="tiny" style="margin-top:5px">Lorem ipsum dolor sit amet, consectetuer adipiscing elit, sed diam nonummy nibh euismod.</p></div>
  <div class="right"><h4 class="sh">Product Specification</h4><table class="spec"><tr><th>Format</th><th>Size</th><th>Metric</th><th>Xx</th></tr><tr><td>Lorem ipsum</td><td>12</td><td>cm</td><td>-</td></tr><tr><td>Lorem ipsum</td><td>256</td><td>mm</td><td>-</td></tr><tr><td>Lorem ipsum</td><td>7128</td><td>mm</td><td>-</td></tr><tr><td>Lorem ipsum</td><td>092</td><td>cm</td><td>-</td></tr><tr><td>Lorem ipsum</td><td>67</td><td>mm</td><td>-</td></tr><tr><td>Lorem ipsum</td><td>89</td><td>mm</td><td>-</td></tr><tr><td>Lorem ipsum</td><td>90</td><td>mm</td><td>-</td></tr><tr><td>Lorem ipsum</td><td>309</td><td>mm</td><td>-</td></tr><tr><td>Lorem ipsum</td><td>596</td><td>mm</td><td>-</td></tr></table></div></div>
  <div class="why"><h4 class="sh">Why you should buy this product?</h4><div class="cols"><p class="tiny">Lorem ipsum dolor sit amet, consectetuer adipiscing elit, sed diam nonummy nibh euismod tincidunt ut laoreet dolore magna aliquam erat volutpat. Ut wisi enim ad minim veniam.</p><p class="tiny">Lorem ipsum dolor sit amet, consectetuer adipiscing elit, sed diam nonummy nibh euismod tincidunt ut laoreet dolore magna aliquam erat volutpat.</p></div></div>
  <div class="prices"><div class="price basic"><span class="tag">BASIC</span><div class="amt">€100</div><p class="cap">Lorem ipsum dolor sit amet, consectetuer adipiscing elit</p></div><div class="price advance"><span class="tag">ADVANCE</span><div class="amt">€600</div><p class="cap">Lorem ipsum dolor sit amet, consectetuer adipiscing elit</p></div><div class="price company"><span class="tag">COMPANY</span><div class="amt">€2500</div><p class="cap">Lorem ipsum dolor sit amet, consectetuer adipiscing elit</p></div></div>
  <div class="contact"><div class="logo-col"><div class="brand"><div class="row"><span class="mark"></span><span class="name">nordlink systems</span></div><span class="sub">by netwave</span></div><div class="partners"><span class="lbl">Mit unsere starken Partnern</span><span class="chip"></span><span class="chip blue"></span><span class="chip red"></span><span class="chip"></span><span class="chip blue"></span><span class="chip red"></span></div></div>
  <div class="addr"><b>Hauptsitz</b>Netwave AG<br>Lindenweg 8<br>6300 Seefeld<br>Telefon +41 00 000 10 10<br>info@netwave-demo.ch</div><div class="addr"><b>Niederlassung</b>Netwave AG<br>Haus am Hang, Rue du Lac 12<br>1260 Valmont<br>Telefon +41 00 000 10 20<br>info@netwave-demo.ch</div></div>
</article>

<article class="slot scale-sm p-r3c">
  <div class="tab">PRODUCT TECHNICAL DATA</div>
  <div class="tech"><div class="left"><h4 class="sh">Production Description</h4><p class="tiny">Lorem ipsum dolor sit amet, consectetuer adipiscing elit, sed diam nonummy nibh euismod tincidunt ut laoreet dolore magna aliquam erat volutpat. Ut wisi enim ad minim veniam, quis nostrud exerci tation ullamcorper suscipit lobortis nisl ut aliquip ex ea commodo consequat.</p><p class="tiny" style="margin-top:5px">Lorem ipsum dolor sit amet, consectetuer adipiscing elit, sed diam nonummy nibh euismod.</p></div>
  <div class="right"><h4 class="sh">Product Specification</h4><table class="spec"><tr><th>Format</th><th>Size</th><th>Metric</th><th>Xx</th></tr><tr><td>Lorem ipsum</td><td>12</td><td>cm</td><td>-</td></tr><tr><td>Lorem ipsum</td><td>256</td><td>mm</td><td>-</td></tr><tr><td>Lorem ipsum</td><td>7128</td><td>mm</td><td>-</td></tr><tr><td>Lorem ipsum</td><td>092</td><td>cm</td><td>-</td></tr><tr><td>Lorem ipsum</td><td>67</td><td>mm</td><td>-</td></tr><tr><td>Lorem ipsum</td><td>89</td><td>mm</td><td>-</td></tr><tr><td>Lorem ipsum</td><td>90</td><td>mm</td><td>-</td></tr><tr><td>Lorem ipsum</td><td>309</td><td>mm</td><td>-</td></tr><tr><td>Lorem ipsum</td><td>596</td><td>mm</td><td>-</td></tr></table></div></div>
  <div class="why"><h4 class="sh">Why you should buy this product?</h4><div class="cols"><p class="tiny">Lorem ipsum dolor sit amet, consectetuer adipiscing elit, sed diam nonummy nibh euismod tincidunt ut laoreet dolore magna aliquam erat volutpat. Ut wisi enim ad minim veniam.</p><p class="tiny">Lorem ipsum dolor sit amet, consectetuer adipiscing elit, sed diam nonummy nibh euismod tincidunt ut laoreet dolore magna aliquam erat volutpat.</p></div></div>
  <div class="prices"><div class="price basic"><span class="tag">BASIC</span><div class="amt">€100</div><p class="cap">Lorem ipsum dolor sit amet, consectetuer adipiscing elit</p></div><div class="price advance"><span class="tag">ADVANCE</span><div class="amt">€600</div><p class="cap">Lorem ipsum dolor sit amet, consectetuer adipiscing elit</p></div><div class="price company"><span class="tag">COMPANY</span><div class="amt">€2500</div><p class="cap">Lorem ipsum dolor sit amet, consectetuer adipiscing elit</p></div><div class="price enterprise"><span class="tag">ENTERPRISE</span><div class="amt">€7500</div><p class="cap">Lorem ipsum dolor sit amet, consectetuer adipiscing elit</p></div></div>
  <div class="contact"><div class="logo-col"><div class="brand"><div class="row"><span class="mark"></span><span class="name">nordlink systems</span></div><span class="sub">by netwave</span></div><div class="partners"><span class="lbl">Mit unsere starken Partnern</span><span class="chip"></span><span class="chip blue"></span><span class="chip red"></span><span class="chip"></span><span class="chip blue"></span><span class="chip red"></span></div></div>
  <div class="addr"><b>Hauptsitz</b>Netwave AG<br>Lindenweg 8<br>6300 Seefeld<br>Telefon +41 00 000 10 10<br>info@netwave-demo.ch</div><div class="addr"><b>Niederlassung</b>Netwave AG<br>Haus am Hang, Rue du Lac 12<br>1260 Valmont<br>Telefon +41 00 000 10 20<br>info@netwave-demo.ch</div></div>
</article>

<article class="slot scale-sm p-r3d">
  <div class="tab">PRODUCT TECHNICAL DATA</div>
  <div class="tech"><div class="left"><h4 class="sh">Production Description</h4><p class="tiny">Lorem ipsum dolor sit amet, consectetuer adipiscing elit, sed diam nonummy nibh euismod tincidunt ut laoreet dolore magna aliquam erat volutpat. Ut wisi enim ad minim veniam, quis nostrud exerci tation ullamcorper suscipit lobortis nisl ut aliquip ex ea commodo consequat.</p><p class="tiny" style="margin-top:5px">Lorem ipsum dolor sit amet, consectetuer adipiscing elit, sed diam nonummy nibh euismod.</p></div>
  <div class="right"><h4 class="sh">Product Specification</h4><table class="spec"><tr><th>Format</th><th>Size</th><th>Metric</th><th>Xx</th></tr><tr><td>Lorem ipsum</td><td>12</td><td>cm</td><td>-</td></tr><tr><td>Lorem ipsum</td><td>256</td><td>mm</td><td>-</td></tr><tr><td>Lorem ipsum</td><td>7128</td><td>mm</td><td>-</td></tr><tr><td>Lorem ipsum</td><td>092</td><td>cm</td><td>-</td></tr><tr><td>Lorem ipsum</td><td>67</td><td>mm</td><td>-</td></tr><tr><td>Lorem ipsum</td><td>89</td><td>mm</td><td>-</td></tr><tr><td>Lorem ipsum</td><td>90</td><td>mm</td><td>-</td></tr><tr><td>Lorem ipsum</td><td>309</td><td>mm</td><td>-</td></tr><tr><td>Lorem ipsum</td><td>596</td><td>mm</td><td>-</td></tr></table></div></div>
  <div class="why split" style="height:200px"><div class="l"><h4 class="sh">Why you should buy this product?</h4><p class="tiny">Lorem ipsum dolor sit amet, consectetuer adipiscing elit, sed diam nonummy nibh euismod tincidunt ut laoreet dolore magna aliquam erat volutpat. Ut wisi enim ad minim veniam, quis nostrud exerci tation ullamcorper suscipit lobortis nisl ut aliquip ex ea commodo consequat.</p><p class="tiny" style="margin-top:5px">Lorem ipsum dolor sit amet, consectetuer adipiscing elit, sed diam nonummy nibh euismod tincidunt ut laoreet dolore magna aliquam erat volutpat. Ut wisi enim ad minim veniam, quis nostrud exerci tation.</p></div>
  <div class="r"><h4 class="sh">Product Price</h4><div class="grid4"><div class="price basic"><span class="tag">BASIC</span><div class="amt">€100</div><p class="cap">Lorem ipsum dolor sit amet, consectetuer adipiscing elit</p></div><div class="price advance"><span class="tag">ADVANCE</span><div class="amt">€600</div><p class="cap">Lorem ipsum dolor sit amet, consectetuer adipiscing elit</p></div><div class="price company"><span class="tag">COMPANY</span><div class="amt">€2500</div><p class="cap">Lorem ipsum dolor sit amet, consectetuer adipiscing elit</p></div><div class="price enterprise"><span class="tag">ENTERPRISE</span><div class="amt">€7500</div><p class="cap">Lorem ipsum dolor sit amet, consectetuer adipiscing elit</p></div></div></div></div>
  <div class="contact"><div class="logo-col"><div class="brand"><div class="row"><span class="mark"></span><span class="name">nordlink systems</span></div><span class="sub">by netwave</span></div><div class="partners"><span class="lbl">Mit unsere starken Partnern</span><span class="chip"></span><span class="chip blue"></span><span class="chip red"></span><span class="chip"></span><span class="chip blue"></span><span class="chip red"></span></div></div>
  <div class="addr"><b>Hauptsitz</b>Netwave AG<br>Lindenweg 8<br>6300 Seefeld<br>Telefon +41 00 000 10 10<br>info@netwave-demo.ch</div><div class="addr"><b>Niederlassung</b>Netwave AG<br>Haus am Hang, Rue du Lac 12<br>1260 Valmont<br>Telefon +41 00 000 10 20<br>info@netwave-demo.ch</div></div>
</article>

</body>
</html>
```